Website Design for Non-profit

We are looking for a new site design for the Patrons of the Northvale Heritage Hall. The current site can be found at
http://www.patrons-nhh.org/nhhindex_e.html
The URL is provided for reference. We want a completely different look and layout which is shown in the specifications document. Visiting the site, you can learn more about the organization.
Initially, we would like a home page, and inside page provided. Once we a home page and inside page are selected, we would like a simple mobile template provided.
I have attached a full description of the project as well as the specifications document and a zip file containing images for the site.
As mentioned in the specs document, we want to include an image of the museum in the header. The zip file is too large for us to upload (80 meg). The zip file can be obtained by clicking this link:
http://qzl.cc/TrVkWp
The zip file contains several exterior photos and you can select the one you feel is most appropriate to your design.
Updates
Project Deadline Extended
Reason: A long weekend is coming up and a few members of the team are unavailable for review.
Project Deadline Extended
Reason: Reviewing designs. Should have a decision next week.
Project Deadline Extended
Reason: We are discussing the designs and looking to reach a consensus. I will be implementing some designs today or tomorrow. Hopefully final selection will be next week.
Project Deadline Extended
Reason: Still reviewing designs. Hope to get a decision soon.
Project Deadline Extended
Reason: Working to finalize the design. Very close.
Project Deadline Extended
Industry/Entity Type
Museum
Look and feel

```html
<!DOCTYPE html>
<html lang="en">
<head>
<meta charset="utf-8">
<title>Patrons of the Northvale Heritage Hall</title>
<link rel="stylesheet" href="https://fonts.googleapis.com/css2?family=Arimo:wght@400;700&display=swap">
<style>
:root{
  --red:#c00a10;
  --red-dark:#8e0408;
  --red-deep:#5a0204;
  --ink:#333;
  --muted:#777;
  --line:#e3e3e3;
  --cream:#fbf4e2;
  --panel:#f4f4f4;
}
*{box-sizing:border-box;margin:0;padding:0}
html,body{width:972px;height:1200px;overflow:hidden;background:#fff;font-family:"Arimo",Arial,sans-serif;color:var(--ink)}
.page{position:relative;width:972px;height:1200px}
.abs{position:absolute}
.header{left:0;top:0;width:972px;height:126px;background:linear-gradient(180deg,#b8070d,#c90c12 60%,#b5070c)}
.header .topline{left:0;top:0;width:972px;height:8px;background:var(--red-deep)}
.brand{left:136px;top:30px;display:flex;align-items:center;gap:8px}
.brand .mark{width:50px;height:42px;background:var(--red-deep);border-radius:50%}
.brand .name{color:var(--red-deep);font-weight:700;font-size:11.5px;line-height:14px;white-space:nowrap}
.tagline{left:445px;top:18px;width:185px;color:#fff;font-size:7.6px;line-height:13px}
.member{left:709px;top:25px;color:#fff;font-size:7.5px}
.member-btn{left:771px;top:22px;width:76px;height:16px;background:#fff;color:#333;font-size:7.5px;text-align:center;line-height:16px;border-radius:2px}
.search{left:670px;top:53px;width:175px;height:23px;background:#fff;border:2px solid #e9525a;display:flex}
.search span{flex:1;font-size:8.5px;color:#999;padding:4px 7px}
.search b{width:22px;background:var(--red);display:flex;align-items:center;justify-content:center}
.nav{left:126px;top:89px;width:720px;height:37px;background:var(--red-dark);display:flex;align-items:center;padding-left:16px}
.nav a{color:#fff;font-weight:700;font-size:10px;text-decoration:none;padding:6px 10px;margin-right:6px}
.nav a.on{background:var(--red);border-radius:2px}
.nav .print{position:absolute;right:0;top:0;height:37px;width:96px;background:#6e0306;display:flex;align-items:center;justify-content:center;gap:8px;color:#fff;font-weight:700;font-size:10px}
.slider-shadow{left:92px;top:356px;width:790px;height:20px;background:radial-gradient(ellipse at center top,rgba(0,0,0,.12),transparent 70%)}
.slider{left:134px;top:133px;width:706px;height:228px;background:linear-gradient(90deg,#d7a28c,#e9b0a0 30%,#3b63c1 50%,#86b47d 75%,#cfd8b0);border:4px solid #fff;box-shadow:0 2px 4px rgba(0,0,0,.15)}
.caption{left:172px;top:178px;width:250px;height:135px;background:rgba(60,50,45,.72);color:#fff;padding:9px 17px}
.caption h2{font-size:9.5px;line-height:13px;margin-bottom:8px}
.caption p{font-size:7.2px;line-height:13px}
.caption .more{font-size:7.2px;margin-top:6px}
.arrow{top:238px}
.info{left:126px;top:386px;width:720px;height:39px;background:var(--panel);border:1px solid #e8e8e8;display:flex;align-items:center;padding-left:13px;gap:11px;font-size:10px;font-weight:700}
.info .i{width:20px;height:20px;border-radius:50%;background:#ddd;color:#fff;font:italic 700 12px Georgia,serif;display:flex;align-items:center;justify-content:center}
.box-head{background:var(--red);color:#fff;font-weight:700;font-size:12.5px;height:28px;line-height:28px;padding-left:10px;border-bottom:1px solid #9c0509}
.sidenav{left:126px;top:440px;width:181px;height:372px;border:1px solid var(--line);border-top:0}
.sidenav ul{list-style:none}
.sidenav li{height:28.8px;border-bottom:1px solid #eee;font-size:10px;color:#444;line-height:28.8px;padding-left:12px}
.sidenav li:last-child{border:0}
.sidenav li::before{content:"›";color:var(--red);font-weight:700;margin-right:10px}
.banner{left:317px;top:440px;width:339px;height:45px;background:linear-gradient(90deg,#222,#555 60%,#888);border:1px solid #ccc;color:#fff;font-size:18px;letter-spacing:-1px;line-height:45px;padding-left:12px}
.tabs{left:317px;top:491px;width:339px;height:28px;background:var(--red);display:flex;align-items:center;padding-left:6px}
.tabs span{color:#fff;font-weight:700;font-size:10px;padding:6px 14px}
.tabs span.on{background:#d9393e}
.middle{left:317px;top:519px;width:339px;height:390px;border:1px solid var(--line);border-top:0}
.feature{left:325px;top:528px;width:323px;height:145px;background:linear-gradient(120deg,#6f6558,#a59685 45%,#c2a57a 70%,#57514a)}
.feature .cap{position:absolute;left:0;bottom:0;width:100%;height:47px;background:rgba(40,35,30,.7);padding:6px 11px;color:#fff}
.feature .cap b{font-size:8.5px;display:block;margin-bottom:3px}
.feature .cap p{font-size:7px;line-height:10px;color:#ddd}
.post{left:325px;width:323px;height:60px;display:flex;gap:10px}
.post .thumb{width:86px;height:51px;background:linear-gradient(135deg,#5a5148,#9c8c7c 50%,#3b3632);flex:none}
.post h3{font-size:9.5px;color:#444;margin:1px 0 5px}
.post p{font-size:7.2px;line-height:11.5px;color:#666}
.post .rm{font-size:7px;color:#999;margin-top:3px}
.divider{left:317px;width:339px;height:1px;background:var(--line)}
.related{left:317px;top:884px;width:339px;height:25px;background:repeating-linear-gradient(135deg,#f3f3f3 0 3px,#fafafa 3px 6px);border-top:1px solid var(--line);font-size:7.5px;color:#555;padding:8px 8px}
.right{left:666px;width:180px}
.vol-text{left:673px;top:477px;width:160px;font-size:7.2px;line-height:11.5px;color:#555}
.target{left:673px;top:524px;width:165px;height:35px;border:1px solid #ddd;display:flex;align-items:center;gap:7px;padding-left:7px}
.target b{color:var(--red);font-size:13px}
.target span{font-size:10.5px;font-weight:700;color:#444}
.donate{left:672px;top:565px;width:167px;height:26px;background:var(--red);color:#fff;font-weight:700;font-size:12px;text-align:center;line-height:26px;border-bottom:2px solid var(--red-dark)}
.speaker{left:666px;width:180px;height:55px;border-bottom:1px solid #e5e5e5;display:flex;gap:9px;padding:3px 7px}
.speaker .ph{width:36px;height:36px;flex:none;border:1px solid #ddd;background:linear-gradient(135deg,#4a443e,#a39686 55%,#2e2b28)}
.speaker b{font-size:7.8px;color:#555;line-height:10px;display:block}
.speaker i{font-size:6.6px;color:#555;display:block;margin-top:4px}
.sponsor-band{left:0;top:920px;width:972px;height:242px;background:var(--cream)}
.sponsor-line{left:134px;top:932px;width:706px;height:6px;background:repeating-linear-gradient(135deg,#ddd 0 2px,#eee 2px 4px)}
.sponsor-title{left:160px;top:922px;background:var(--cream);padding:0 8px;color:var(--red);font-weight:700;font-size:11.5px}
.carousel{left:126px;top:940px;width:720px;height:76px;background:#fff;border:1px solid #e8e0c8;display:flex;align-items:center}
.carousel .nav-btn{width:21px;height:74px;background:#eee;display:flex;align-items:center;justify-content:center;color:#444;font-size:12px;flex:none}
.carousel .items{flex:1;display:flex;justify-content:space-around;align-items:center}
.carousel .sp{display:flex;align-items:center;gap:4px;font-size:9px;font-weight:700;color:#555}
.carousel .sp i{width:10px;height:10px;background:#7a9;display:block;border-radius:50%}
.foot h4{color:var(--red);font-size:11.5px;margin-bottom:4px}
.foot p{font-size:7.2px;line-height:9.5px;color:#555}
.vsep{width:1px;background:#ddd;top:1046px;height:70px}
.social{display:flex;gap:5px;margin-top:3px}
.social span{font-size:8px;font-weight:700;color:#fff;background:#3b5998;padding:3px 4px}
.social span.b{background:var(--red)}
.partner{left:686px;width:127px;height:39px;background:#fff;border:1px solid #ccc;display:flex;align-items:center;justify-content:center;gap:6px;font-weight:700;font-size:10.5px;color:#222}
.partner i{width:10px;height:10px;background:#222;display:block}
.bottomnav{left:126px;top:1130px;width:720px;height:32px;background:#fff;border:1px solid #eee;display:flex;align-items:center;padding-left:13px;font-size:7.5px;color:#444}
.bottomnav span{padding:0 13px 0 0}
.bottomnav span+span::before{content:"|";color:#aaa;margin-right:13px}
</style>
</head>
<body>
<div class="page">
  <header class="abs header">
    <div class="abs topline"></div>
    <div class="abs brand"><div class="mark"></div><div class="name">NORTHVALE HERITAGE HALL<br>SALLE DU PATRIMOINE NORTHVALE</div></div>
    <div class="abs tagline">We're working with you to make a positive impact around the world in more than 30 countries, all 50 United States and your backyard. 1800.555.014 [Toll-free Canada. only]</div>
    <div class="abs member">Not a member?</div>
    <div class="abs member-btn">Member Login</div>
    <div class="abs search"><span>Enter any Keyword</span><b><svg width="11" height="11" viewBox="0 0 12 12"><circle cx="5" cy="5" r="3.6" fill="none" stroke="#fff" stroke-width="1.6"/><path d="M7.6 7.6 11 11" stroke="#fff" stroke-width="1.8"/></svg></b></div>
    <nav class="abs nav">
      <a class="on">Home</a><a>About</a><a>Support PNHH</a><a>Events</a><a>Projects &amp; Programs</a><a>Meet the Friends</a><a>Publications</a>
      <div class="print"><svg width="16" height="15" viewBox="0 0 16 15"><rect x="4" y="0" width="8" height="5" fill="#fff"/><rect x="0" y="5" width="16" height="6" rx="1" fill="#fff"/><rect x="4" y="9" width="8" height="6" fill="#ddd" stroke="#6e0306"/></svg>Print Page</div>
    </nav>
  </header>

  <div class="abs slider-shadow"></div>
  <div class="abs slider" role="img" aria-label="Photo of smiling children holding a cardboard sign about giving"></div>
  <div class="abs caption">
    <h2>Sollicitudin a lacinia eufermentum etellus vestibulum libero nibh.</h2>
    <p>Lorem ipsum dolor sit amet, consectetur adipiscing elit. Morbi hendrerit luctus tincidunt. Nulla eu vehicula mauris. Integer viverra fermentum quam, id sagittis massa tempor eu. Nunc magna sapien, sollicitudin a lacinia eu, fermentum et tellus. Vestibulum libero nibh, tristique ac tempus vel.</p>
    <div class="more">» Read More</div>
  </div>
  <svg class="abs arrow" style="left:148px" width="20" height="30" viewBox="0 0 20 30"><path d="M16 3 4 15l12 12" fill="none" stroke="rgba(255,255,255,.75)" stroke-width="5"/></svg>
  <svg class="abs arrow" style="left:804px" width="20" height="30" viewBox="0 0 20 30"><path d="M4 3l12 12L4 27" fill="none" stroke="rgba(255,255,255,.75)" stroke-width="5"/></svg>

  <div class="abs info"><span class="i">i</span>Lorem ipsum dolor sit amet, consectetur adipiscing elit. Integer porttitor lacus vel dolor accumsan tempor. Read More..
    <svg style="margin-left:24px" width="8" height="12" viewBox="0 0 8 12"><path d="M1 5 4 2l3 3M1 7l3 3 3-3" fill="none" stroke="#333" stroke-width="1.6"/></svg>
    <svg style="position:absolute;right:5px;top:0" width="10" height="10" viewBox="0 0 10 10"><circle cx="5" cy="5" r="5" fill="#444"/><path d="M3 3l4 4M7 3 3 7" stroke="#fff" stroke-width="1.3"/></svg>
  </div>

  <aside class="abs sidenav">
    <div class="box-head">SECONDARY NAVIGATION</div>
    <ul>
      <li>ABOUT US</li><li>DEVINIR A FRIEND</li><li>PHOTO GALLERIES</li><li>BOOKS</li><li>EVENTS</li><li>PERSONEL ADS</li><li>PROGRAMS</li><li>TREASURES MEMBERS</li><li>CONNECTIONS</li><li>GIVE A GIFT</li><li>CONTACT PNHH</li><li>ENGLISH</li>
    </ul>
  </aside>

  <div class="abs banner" role="img" aria-label="Happening today banner photo">Happening Today (468 x 60)</div>
  <div class="abs tabs"><span class="on">Welcome</span><span>Video</span></div>
  <div class="abs middle"></div>
  <div class="abs feature" role="img" aria-label="Photo of a child holding a cardboard help sign">
    <div class="cap"><b>Fusce faucibus mauris vitae orci</b><p>Donec nec tincidunt felis. Fusce ac lorem felis. Aliquam erat volutpat. Aliquam ornare sem eu ante sollicitudin malesuada. Class aptent</p></div>
  </div>
  <div class="abs post" style="top:690px"><div class="thumb" role="img" aria-label="Photo of a committee meeting"></div><div><h3>Suspendisse potenti. Nulla</h3><p>Nam condimentum molestie bibendum. Nam auctor venenatis urna, sed consequat enim egestas a. Nunc sed</p><div class="rm">› Read more</div></div></div>
  <div class="abs divider" style="top:749px"></div>
  <div class="abs post" style="top:757px"><div class="thumb" role="img" aria-label="Photo of two men at an event"></div><div><h3>Class aptent taciti sociosqu ad...</h3><p>Sed vitae odio urna. Cras iaculis tempor arcu, a egestas nisi viverra non. Cras tempus dui blandit tellus</p><div class="rm">› Read more</div></div></div>
  <div class="abs divider" style="top:817px"></div>
  <div class="abs post" style="top:824px"><div class="thumb" role="img" aria-label="Photo of two speakers"></div><div><h3>Cras vel hendrerit leo. Integer...</h3><p>Cras vel hendrerit leo. Integer tortor leo, gravida non pretium a, gravida quis est. Donec vitae nisl</p><div class="rm">› Read more</div></div></div>
  <div class="abs related">View related posts</div>

  <div class="abs right box-head" style="top:440px">BECOME A VOLUNTEER</div>
  <div class="abs vol-text">Lorem ipsum dolor sit amet, consectetur adipiscing elit Nam pulvinar.</div>
  <div class="abs target"><b>$2,500</b><span>Target, $25,000</span></div>
  <div class="abs donate">DONATE NOW</div>
  <div class="abs right box-head" style="top:608px">SPEAKER'S BUREAU</div>
  <div class="abs speaker" style="top:641px"><div class="ph" role="img" aria-label="Speaker photo"></div><div><b>Class aptent taciti sociosqu ad litora torquent</b><i>March 26, 2012, 0 comments</i></div></div>
  <div class="abs speaker" style="top:696px"><div class="ph" role="img" aria-label="Speaker photo"></div><div><b>Cras vel hendrerit leo. Integer tortor leo</b><i>March 26, 2012, 0 comments</i></div></div>
  <div class="abs speaker" style="top:752px"><div class="ph" role="img" aria-label="Speaker photo"></div><div><b>Class aptent taciti sociosqu ad litora torquent</b><i>March 26, 2012, 0 comments</i></div></div>
  <div class="abs speaker" style="top:807px"><div class="ph" role="img" aria-label="Speaker photo"></div><div><b>Cras vel hendrerit leo. Integer tortor leo</b><i>March 26, 2012, 0 comments</i></div></div>
  <div class="abs speaker" style="top:863px;border:0"><div class="ph" role="img" aria-label="Speaker photo"></div><div><b>Class aptent taciti sociosqu ad litora torquent</b><i>March 26, 2012, 0 comments</i></div></div>

  <div class="abs sponsor-band"></div>
  <div class="abs sponsor-line"></div>
  <div class="abs sponsor-title">Our Sponsors</div>
  <div class="abs carousel">
    <div class="nav-btn">‹</div>
    <div class="items">
      <div class="sp"><i></i>Ardley Aid</div>
      <div class="sp">Quenmore Homes</div>
      <div class="sp">Tellbright Line</div>
      <div class="sp"><i style="background:#23408f;border-radius:0"></i>Pellowick Trust</div>
      <div class="sp">Marrowfield Walk</div>
      <div class="sp"><i style="background:#e8b420"></i>Brenhale Exchange</div>
      <div class="sp">Orielvale Care</div>
    </div>
    <div class="nav-btn">›</div>
  </div>

  <div class="abs foot" style="left:126px;top:1034px;width:172px">
    <h4>About Us</h4>
    <p style="text-align:justify">Lorem ipsum dolor sit amet, consectetur adipiscing elit. Nam pulvinar, odio eu consectetur porta, libero orci tempor felis, a adipiscing diam ipsum in enim. Donec hendrerit dictum quam, a tincidunt neque vulputate nec. Proin nec sollicitudin augue.</p>
  </div>
  <div class="abs vsep" style="left:308px"></div>
  <div class="abs foot" style="left:319px;top:1034px;width:150px">
    <h4>Contact Us</h4>
    <p>Patrons of the Northvale Heritage Hall</p>
    <p style="margin-top:11px">12 Harbour Lane, Northvale, Ontario K0A 1B2, Canada - 43680.</p>
    <p style="margin-top:11px">Fax - +1 555 010 7894<br>Email - http://www.patrons-nhh.org</p>
  </div>
  <div class="abs vsep" style="left:475px"></div>
  <div class="abs foot" style="left:486px;top:1034px">
    <h4>Social Network</h4>
    <div class="social"><span>Plazio</span><span class="b">Vidmora</span></div>
  </div>
  <div class="abs vsep" style="left:655px"></div>
  <div class="abs partner" style="top:1033px"><i></i>CORVANE</div>
  <div class="abs partner" style="top:1080px">PNHH · APSN</div>

  <div class="abs bottomnav">
    <span>Home</span><span>About</span><span>Support PNHH</span><span>Events</span><span>Projects &amp; Programs</span><span>Meet the Friends</span><span>Publications</span>
  </div>
</div>
</body>
</html>
```